Talcott Land Surveyors Business Card

We are a land surveying company looking for a business card with a clean, sharp design. We would like for our design to portray our logo on one side, and contact information on the other w/ or w/o logo. Our colors preferred are navy blue, grey/silver, white and black. thank you!

Industry/Entity Type

Surveyor

Contact Information for Business Card

Talcott Land Surveyors
Gordon Pavlikova, P.L.S.
(781) 555-0193
Talcottlandsurveyors@mailbox.example
Talcottlandsurveyors.example
287 Willowmere Lane, Reading MA 01999

Requirements
Must have
• 1. Company Name
2. Personal name and title
3. phone number
4. email.
5. website
6. address

```html
<!DOCTYPE html>
<html lang="en">
<head>
<meta charset="utf-8">
<title>Talcott Land Surveyors – Business Card</title>
<link href="https://fonts.googleapis.com/css2?family=Michroma&display=swap" rel="stylesheet">
<style>
  :root {
    --backdrop: #1b1b1c;
    --kraft-light: #dfbf95;
    --kraft-mid: #c79e6c;
    --kraft-dark: #a9794a;
    --ink: #141210;
    --rule: #5b4630;
  }
  * { box-sizing: border-box; margin: 0; padding: 0; }
  html, body {
    width: 1093px;
    height: 1200px;
    overflow: hidden;
    background: var(--backdrop);
  }
  .canvas {
    position: relative;
    width: 1093px;
    height: 1200px;
    font-family: "Michroma", sans-serif;
    color: var(--ink);
  }
  .card {
    position: absolute;
    left: 264px;
    width: 580px;
    height: 357px;
    background: linear-gradient(135deg, var(--kraft-light) 0%, var(--kraft-mid) 55%, var(--kraft-dark) 100%);
  }
  .card--contact { top: 226px; }
  .card--brand { top: 620px; }

  .line {
    position: absolute;
    left: 0;
    width: 100%;
    text-align: center;
    transform: translateY(-50%);
    white-space: nowrap;
    text-transform: uppercase;
  }
  .holder-name { top: 103px; font-size: 14px; letter-spacing: 0.06em; }
  .phone { top: 142px; font-size: 12px; letter-spacing: 0.22em; }
  .email { top: 165px; font-size: 10px; letter-spacing: 0.14em; }
  .website { top: 188px; font-size: 10px; letter-spacing: 0.14em; }
  .company { top: 232px; font-size: 12px; letter-spacing: 0.18em; }
  .address { top: 254px; font-size: 12px; letter-spacing: 0.18em; text-transform: none; font-variant: small-caps; }

  .rule {
    position: absolute;
    left: 209px;
    width: 162px;
    height: 1px;
    background: var(--rule);
  }
  .rule--top { top: 122px; }
  .rule--bottom { top: 211px; }

  .brand-mark {
    position: absolute;
    left: 50%;
    top: 80px;
    transform: translateX(-50%);
  }
  .brand-name {
    top: 248px;
    font-size: 19px;
    letter-spacing: 0.16em;
  }
</style>
</head>
<body>
<main class="canvas">
  <section class="card card--contact" aria-label="Contact side">
    <p class="line holder-name">Gordon Pavlikova, P.L.S.</p>
    <span class="rule rule--top"></span>
    <p class="line phone">(781) 555-0193</p>
    <p class="line email">Talcottlandsurveyors@mailbox.example</p>
    <p class="line website">www.Talcottlandsurveyors.example</p>
    <span class="rule rule--bottom"></span>
    <p class="line company">Talcott Land Surveyors</p>
    <p class="line address">287 Willowmere Lane Reading MA 01999</p>
  </section>

  <section class="card card--brand" aria-label="Brand side">
    <svg class="brand-mark" width="100" height="100" viewBox="0 0 100 100" aria-hidden="true">
      <circle cx="50" cy="50" r="42" fill="none" stroke="var(--ink)" stroke-width="2"/>
    </svg>
    <p class="line brand-name">Talcott Land Surveyors</p>
  </section>
</main>
</body>
</html>
```